Online tuition webpage design needed

Hi,
We are starting up an online tuition website for non- English speakers wishing to take an QRAVE test.

The webpage must include a place for people to enroll online in the course.
The home page must have:
• room for a logo (coming shortly, blue in colour)
• different packages of online tuition and coinvy
• tool bar showing different pages
• perhaps a video, small pictures

This is my site currently:-

www.lernmarowebtutor.example

as you can see, I am not very sure how to create a website … The large logo is what I would like to use, but I project has not been finalized yet. Please note, I don’t like the logo being that large!

Sites that are similar to what I am doing and like the design of are:

http://www.quorvapath.example.au/fees

https://www.brantiq9.example/index.php

http://www.tutorhalvekmorris.example.uk/index.html

http://www.vorplaneexam.example/

One thing I need is a place for student s to enroll, and if possible, I would like to use plovix to create exercises for students.
Currently, my site is using sitequill. My preference is to use plovix for online activities. I am not sure if I can use both.
Thanks in advance

Target Market(s)

people wising to take an QRAVE test (English proficiency test)

Industry/Entity Type

Online

Colors
3276b5
0292cd

Requirements
Must have
• a place for enrollment and admin login for students
plovix
video
talvo, gatherly, chirrup logos
Nice to have
• a booking calender
Should not have
• too much clutter. must be clean and professional looking

```html
<!DOCTYPE html>
<html lang="en">
<head>
<meta charset="utf-8">
<title>QRAVE Online Tuition</title>
<link href="https://fonts.googleapis.com/css2?family=Open+Sans:wght@400;600;700;800&family=Oswald:wght@500;600&display=swap" rel="stylesheet">
<style>
:root{
  --brand:#3276b5;
  --sky:#0292cd;
  --navy:#1c2836;
  --navy-2:#2a3a4d;
  --mist:#e8edf2;
  --ink:#3a4652;
  --muted:#7a8794;
  --footer:#285a88;
  --footer-deep:#1f4a72;
  --white:#ffffff;
}
*{box-sizing:border-box;margin:0;padding:0}
html,body{width:900px;height:1200px;overflow:hidden}
body{font-family:"Open Sans",Arial,sans-serif;color:var(--ink);background:var(--white);font-size:11px;line-height:1.5}
.page{position:relative;width:900px;height:1200px;overflow:hidden}
.wrap{width:640px;margin:0 auto;position:relative}

/* header */
.site-header{height:84px}
.site-header .wrap{height:84px;display:flex;align-items:center;justify-content:space-between}
.brand{display:flex;align-items:center;gap:10px}
.brand-dot{width:30px;height:30px;border-radius:50%;background:var(--brand)}
.brand-name{font-weight:800;font-size:28px;color:var(--brand);line-height:1}
.brand-tag{font-size:12px;color:var(--brand);font-weight:600;margin-top:2px}
.top-social{display:flex;gap:8px;font-size:9px;color:var(--muted);align-self:flex-start;margin-top:14px}

/* nav */
.main-nav{height:24px;background:linear-gradient(var(--sky),var(--brand))}
.main-nav ul{list-style:none;display:flex;height:24px;align-items:stretch}
.main-nav li{font-size:9.5px;color:var(--white);padding:0 13px;display:flex;align-items:center;border-right:1px solid rgba(255,255,255,.25)}
.main-nav li.active{background:var(--navy)}

/* hero */
.hero{height:237px;background:linear-gradient(135deg,var(--navy-2),var(--navy));overflow:hidden}
.hero .wrap{height:237px}
.hero-copy{position:absolute;left:20px;top:34px;color:var(--white)}
.hero-title{font-family:"Oswald",Arial,sans-serif;font-weight:600;font-size:34px;line-height:1.05;letter-spacing:.5px}
.hero-sub{font-family:"Oswald",Arial,sans-serif;font-weight:500;font-size:17px;line-height:1.15;margin-top:4px;width:330px;color:#dfe6ee}
.hero-handle{display:flex;align-items:center;gap:8px;margin-top:18px;font-size:10px;font-weight:600}
.hero-handle span.dot{width:18px;height:18px;border-radius:50%;background:var(--sky)}
.btn{display:inline-block;background:var(--sky);color:var(--white);font-weight:700;text-transform:uppercase;border-radius:3px}
.hero .btn{margin-top:16px;padding:7px 22px;font-size:13px}
.hero-photo{position:absolute;right:-10px;top:0;width:220px;height:237px;background:radial-gradient(circle at 50% 45%,#e98a5a 0,#8a5a48 35%,#2f3a48 75%)}

/* welcome */
.welcome{height:220px;background:var(--mist);padding-top:18px}
.section-title{font-size:18px;font-weight:700;color:var(--brand)}
.welcome-text{font-size:9.5px;color:var(--muted);margin-top:4px;width:470px}
.cards{display:flex;gap:12px;margin-top:14px}
.card{width:205px;background:var(--white);border:1px solid #d5dde5}
.card-head{background:var(--brand);color:var(--white);font-size:10px;font-weight:600;padding:5px 10px}
.card-media{height:82px;background:linear-gradient(135deg,#c9d6e2,#9fb3c6);margin:6px}

/* about */
.about{height:190px;padding-top:18px}
.about-copy{width:370px}
.about-lead{font-size:11px;color:var(--brand);line-height:1.45}
.about-list{list-style:none;margin-top:8px}
.about-list li{font-size:10.5px;color:var(--brand);display:flex;align-items:center;gap:8px;line-height:1.75}
.about-list li::before{content:"";width:7px;height:7px;border-radius:50%;background:var(--sky)}
.about-mark{position:absolute;right:30px;top:4px;width:140px;height:140px;border-radius:50%;background:var(--mist);display:flex;align-items:center;justify-content:center;font-weight:800;font-size:26px;color:var(--brand)}

/* booking */
.booking{height:205px;background:var(--sky);color:var(--white);padding-top:22px}
.booking .wrap{display:flex;gap:20px}
.booking-info{width:210px}
.booking-title{font-size:17px;font-weight:700;letter-spacing:.5px}
.booking-text{font-size:8.5px;line-height:1.55;margin-top:8px;color:#e4f4fb}
.booking-form{width:190px;display:flex;flex-direction:column;gap:6px;padding-top:4px}
.field{background:var(--white);color:var(--muted);font-size:8.5px;height:18px;padding:2px 6px;border-radius:2px}
.field.tall{height:50px}
.calendar{width:200px}
.cal-head{font-size:10px;font-weight:700;text-align:center;background:var(--brand);padding:3px 0}
.cal-grid{display:grid;grid-template-columns:repeat(7,1fr);gap:2px;margin-top:2px}
.cal-grid span{background:rgba(255,255,255,.9);color:var(--ink);font-size:7.5px;text-align:center;height:17px;line-height:17px}
.cal-grid span.on{background:var(--brand);color:var(--white)}
.booking .btn{background:var(--navy);font-size:9px;padding:4px 14px;margin-top:8px;float:right}

/* footer */
.site-footer{height:200px;background:var(--footer);color:var(--white);padding-top:26px}
.site-footer .wrap{display:flex;gap:50px}
.foot-col h4{font-size:12px;font-weight:700;margin-bottom:8px}
.foot-col li{list-style:none;font-size:10px;line-height:1.75;color:#d6e4f1}
.foot-brand{margin-left:auto;display:flex;align-items:center;gap:8px;align-self:center}
.foot-brand .brand-dot{background:var(--white)}
.foot-brand .brand-name{color:var(--white);font-size:24px}
.foot-brand .brand-tag{color:var(--white)}
.bottom-bar{height:40px;background:var(--footer-deep);color:#b9cde0;font-size:8.5px}
.bottom-bar .wrap{height:40px;display:flex;align-items:center;justify-content:space-between}
</style>
</head>
<body>
<div class="page">
  <header class="site-header">
    <div class="wrap">
      <div class="brand">
        <span class="brand-dot"></span>
        <div><div class="brand-name">QRAVE</div><div class="brand-tag">Online Tuition</div></div>
      </div>
      <div class="top-social"><span>gatherly</span><span>chirrup</span><span>talvo</span></div>
    </div>
  </header>

  <nav class="main-nav">
    <div class="wrap">
      <ul>
        <li class="active">Home</li>
        <li>Tuition Packages</li>
        <li>Weekly Tips and Comments</li>
        <li>Reading</li>
        <li>Speaking</li>
        <li>Listening</li>
        <li>Writing</li>
      </ul>
    </div>
  </nav>

  <section class="hero">
    <div class="wrap">
      <div class="hero-copy">
        <h1 class="hero-title">ONLINE QRAVE TUITION</h1>
        <p class="hero-sub">PROFESSIONAL HELP FOR PEOPLE TAKING AN QRAVE TEST</p>
        <div class="hero-handle"><span class="dot"></span>QRAVE.ONLINETUITION</div>
        <a class="btn">Contact Us</a>
      </div>
      <div class="hero-photo" role="img" aria-label="Photo of a student sitting with a laptop"></div>
    </div>
  </section>

  <section class="welcome">
    <div class="wrap">
      <h2 class="section-title">Welcome To QRAVE Online Tuition</h2>
      <p class="welcome-text">International English Tuition: We are your customers first. We listen to you and help you find what you need. If your work help...</p>
      <div class="cards">
        <div class="card"><div class="card-head">QRAVE Online Tuition</div><div class="card-media" role="img" aria-label="Photo for online tuition"></div></div>
        <div class="card"><div class="card-head">Tutorial Packages</div><div class="card-media" role="img" aria-label="Photo for tutorial packages"></div></div>
        <div class="card"><div class="card-head">Weekly Tips and Comments</div><div class="card-media" role="img" aria-label="Photo for weekly tips"></div></div>
      </div>
    </div>
  </section>

  <section class="about">
    <div class="wrap">
      <div class="about-copy">
        <p class="about-lead">We put you first. We listen to you and help you find what you need. If you want help in passing an QRAVE test, we can help you with:</p>
        <ul class="about-list">
          <li>Lessons in reading, writing, listening and speaking</li>
          <li>Professional teacher feedback and tips</li>
          <li>talvo and practise with native speakers</li>
          <li>Quick Turnaround</li>
          <li>Friendly and Approachable teachers</li>
        </ul>
      </div>
      <div class="about-mark">QRAVE</div>
    </div>
  </section>

  <section class="booking">
    <div class="wrap">
      <div class="booking-info">
        <h2 class="booking-title">BOOKING CALENDER</h2>
        <p class="booking-text">Choose a time that suits you and book a private lesson with one of our tutors. Sessions run every weekday and on Saturday mornings. Pick a date on the calendar, add your details in the form and press book now. We will confirm by email within one working day.</p>
      </div>
      <div class="booking-form">
        <div class="field">Name</div>
        <div class="field">Email</div>
        <div class="field">Phone</div>
        <div class="field tall">Message</div>
      </div>
      <div class="calendar">
        <div class="cal-head">June</div>
        <div class="cal-grid">
          <span>1</span><span>2</span><span>3</span><span>4</span><span>5</span><span>6</span><span>7</span>
          <span>8</span><span>9</span><span>10</span><span class="on">11</span><span>12</span><span>13</span><span>14</span>
          <span>15</span><span>16</span><span>17</span><span>18</span><span>19</span><span>20</span><span>21</span>
          <span>22</span><span>23</span><span>24</span><span>25</span><span>26</span><span>27</span><span>28</span>
          <span>29</span><span>30</span><span></span><span></span><span></span><span></span><span></span>
        </div>
        <a class="btn">Book Now</a>
      </div>
    </div>
  </section>

  <footer class="site-footer">
    <div class="wrap">
      <div class="foot-col"><h4>Our Courses</h4><ul><li>QRAVE Express</li><li>QRAVE Master</li><li>QRAVE Master Plus</li></ul></div>
      <div class="foot-col"><h4>More Info</h4><ul><li>Fees</li><li>Agent Host</li><li>About Us</li></ul></div>
      <div class="foot-col"><h4>Social Media</h4><ul><li>gatherly</li><li>chirrup</li><li>Linkora</li><li>talvo</li></ul></div>
      <div class="foot-brand">
        <span class="brand-dot"></span>
        <div><div class="brand-name">QRAVE</div><div class="brand-tag">Online Tuition</div></div>
      </div>
    </div>
  </footer>
  <div class="bottom-bar">
    <div class="wrap"><span>Terms of Use &nbsp;|&nbsp; Privacy Statement &nbsp;|&nbsp; Sitemap</span><span>© QRAVE Online Tuition. All Rights Reserved.</span></div>
  </div>
</div>
</body>
</html>
```